Martial Arts Website

Redevelopment of existing martial arts website.

The academy teaches traditional shaolin martial arts, including Shaolin Kung Fu, Wu Shu, Tai Chi, Qigong and Wing Chun and the site needs to reflect the traditional roots (eg, no tacky boxing imagery)

Existing website is www.copperheron.com.au to get a feel for the desired color scheme (black, green and red). The exact colors can be tweaked though. Please only reuse the logo and font (Karate) - there isnt anything else from the current design that needs to remain.

The current website includes links to a YouTube channel that includes demonstrations of the training conducted to better guide the design.

The new website site map will be:
1. Home
2. Programs - summary page describing each form of training
a. Tiny Sparrows
b. Kids Kung Fu
c. Youth Kung Fu
d. Adults Kung Fu
e. Wing Chun
f. Tai Chi & Qigong
g. Weaponry Classes
h. 48 Paths of Mountain Endurance Program
i. Acrobatics and Wu Shu
j. Fitness Boxing
3. Timetable
4. Coaches - summary page describing all coaches
a. Sifu (Master)
b. Sihing Lars
c. Sihing Kit
d. Sihing Gordon
X. ... up to 10 or so coaches
5. Member Zone
6. Contact Us
Updates

Logo now attached to brief - sorry I only have it in PDF

Just to clarify, I am only expecting a PSD design - no HTML required

Project Deadline Extended
Reason: Thanks for the designs, we love a lot of them just require a little extra time to tweak the designs and establish the potential. Thanks for your understanding and efforts.

Target Market(s)

Parents, teenagers, young adults, adults, elderly

Industry/Entity Type

Training

Requirements
Must have
• Chinese kung fu dragon imagery throughout the background
Links to Facebook and YouTube channel
Promo/icon in the header "Try 2 free classes now"
Home page should include an embedded YouTube video

```html
<!DOCTYPE html>
<html lang="en">
<head>
<meta charset="utf-8">
<title>Copper Heron Martial Arts Academy</title>
<link rel="stylesheet" href="https://fonts.googleapis.com/css2?family=Signika:wght@400;600&family=PT+Sans:wght@400;700&display=swap">
<style>
  :root{
    --page:#0b0b0b;
    --stripe-a:#1f5e1f;
    --stripe-b:#0f3a10;
    --nav-top:#22b322;
    --nav-bottom:#087008;
    --nav-text:#0a1a0a;
    --tab:#0d6a0d;
    --dropdown:#0b5a0b;
    --link-green:#52d652;
    --heading-green:#38c238;
    --side-bg:#062806;
    --side-border:#0e4a0e;
    --white:#ffffff;
    --footer-text:#e6e6e6;
    --muted:#8c8c8c;
    --ring:#3fc33f;
  }
  *{margin:0;padding:0;box-sizing:border-box}
  html,body{width:932px;height:1200px;overflow:hidden;background:var(--page)}
  body{position:relative;font-family:"PT Sans",Arial,sans-serif;color:var(--white)}
  .masthead-bg{position:absolute;left:0;top:0;width:932px;height:974px;
    background:linear-gradient(160deg,var(--stripe-a),var(--stripe-b) 60%,#0a2a0a)}
  .frame{position:absolute;left:14px;top:98px;width:904px;height:876px;background:#050505;border-radius:6px 6px 0 0}
  .brand{position:absolute;top:48px;font-family:"Signika",sans-serif;font-weight:600;font-size:21px;
    letter-spacing:1px;text-transform:uppercase;color:var(--white)}
  .brand-left{left:186px}
  .brand-right{left:527px}
  .nav{position:absolute;left:23px;top:105px;width:884px;height:59px;border-radius:5px 5px 0 0;
    background:linear-gradient(var(--nav-top),var(--nav-bottom))}
  .nav a{position:absolute;top:24px;font-family:"Signika",sans-serif;font-size:15px;color:var(--nav-text);
    text-decoration:none;text-transform:uppercase}
  .nav .small{font-size:13px;top:26px}
  .nav .active{left:104px;top:9px;width:105px;height:50px;background:var(--tab);border-radius:6px 6px 0 0;
    color:var(--link-green);text-align:center;padding-top:15px}
  .badge{position:absolute;left:364px;top:18px;width:160px;height:160px;border-radius:50%;
    background:#101010;border:6px solid var(--ring);box-shadow:0 0 0 3px #0a4a0a}
  .hero{position:absolute;left:25px;top:167px;width:881px;height:327px;
    background:linear-gradient(180deg,#c9c4bd 0%,#b9aea3 40%,#c98e6e 70%,#b87458 100%)}
  .dropdown{position:absolute;left:127px;top:162px;width:237px;height:116px;background:var(--dropdown);
    border-radius:0 6px 6px 6px}
  .dropdown a{position:absolute;font-family:"Signika",sans-serif;font-size:12.5px;color:var(--link-green);text-decoration:none;white-space:nowrap}
  .main{position:absolute;left:42px;top:516px;width:572px}
  h1,h2{font-family:"Signika",sans-serif;font-weight:400;color:var(--heading-green)}
  h1{font-size:16.5px;margin-bottom:6px}
  .intro{font-size:11.3px;line-height:16.4px;text-align:justify;margin-bottom:5px}
  .program{font-size:10px;line-height:16.4px;margin-top:12px}
  .program b{font-family:"Signika",sans-serif;font-weight:400;font-size:12.5px;color:var(--heading-green)}
  .sidebar{position:absolute;left:648px;top:499px;width:251px;height:463px;background:var(--side-bg);
    border:1px solid var(--side-border);border-radius:4px;padding:17px 6px 0 18px}
  .sidebar h2{font-size:16.5px;margin-bottom:12px}
  .sidebar h3{font-family:"PT Sans",sans-serif;font-weight:700;font-size:10.5px;color:var(--white);margin-bottom:6px}
  .sidebar p{font-size:10px;line-height:16.4px;color:var(--link-green);margin-bottom:8px}
  .footer{position:absolute;left:0;top:974px;width:932px;height:226px;background:#000;border-top:1px solid #222}
  .footer ul{position:absolute;top:24px;list-style:none}
  .footer li{font-size:11.5px;color:var(--footer-text);height:27.3px;padding-left:15px;position:relative}
  .footer li::before{content:"";position:absolute;left:0;top:4px;border-left:5px solid #bbb;border-top:4px solid transparent;border-bottom:4px solid transparent}
  .foot-mark{position:absolute;left:714px;top:15px;width:110px;height:110px;border-radius:50%;
    border:5px solid var(--ring);background:#0c0c0c;display:flex;align-items:center;justify-content:center;
    text-align:center;font-family:"Signika",sans-serif;font-size:12px;color:var(--white)}
  .copyright{position:absolute;left:43px;top:162px;font-size:11px;color:var(--muted)}
</style>
</head>
<body>
  <div class="masthead-bg" role="img" aria-label="Green dragon-scale textured background"></div>
  <div class="frame"></div>

  <div class="brand brand-left">Copper Heron</div>
  <div class="brand brand-right">Martial Arts Academy</div>

  <nav class="nav">
    <a style="left:46px" href="#">Home</a>
    <a class="active" href="#">Programs</a>
    <a style="left:226px" href="#">Timetable</a>
    <a class="small" style="left:553px" href="#">Coaches</a>
    <a class="small" style="left:634px" href="#">Member Zone</a>
    <a class="small" style="left:750px" href="#">Contact Us</a>
  </nav>

  <div class="hero" role="img" aria-label="Photo of a master leading a tai chi class in a sports hall"></div>

  <div class="badge"></div>

  <div class="dropdown">
    <a style="left:19px;top:12px" href="#">Tiny Sparrows</a>
    <a style="left:19px;top:36px" href="#">Kids Kung Fu</a>
    <a style="left:19px;top:61px" href="#">Youth Kung Fu</a>
    <a style="left:19px;top:85px" href="#">Adults Kung Fu</a>
    <a style="left:121px;top:12px" href="#">Wing Chun</a>
    <a style="left:121px;top:36px" href="#">Tai Chi &amp; Qigong</a>
    <a style="left:121px;top:61px" href="#">Weaponry Classes</a>
    <a style="left:121px;top:85px" href="#">48 Paths of Endurance</a>
  </div>

  <section class="main">
    <h1>Welcome to Copper Heron Martial Arts Academy - NSW Australia</h1>
    <p class="intro">Lorem ipsum dolor sit amet, consectetuer adipiscing elit. Nam cursus. Morbi ut mi. Nullam enim leo, egestas id, condimentum at, laoreet mattis, massa. Sed eleifend nonummy diam. Praesent mauris ante, elementum et, bibendum at, posuere sit amet, nibh. Duis tincidunt lectus quis dui viverra vestibulum.</p>
    <p class="intro">Suspendisse vulputate aliquam dui. Nulla elementum dui ut augue. Aliquam vehicula mi at mauris. Maecenas placerat, nisl at consequat rhoncus, sem nunc gravida justo, quis eleifend arcu velit quis lacus. Morbi magna magna, tincidunt a, mattis non, imperdiet vitae, tellus. Sed odio est, auctor ac, sollicitudin in, consequat vitae, orci. Fusce id felis. Vivamus sollicitudin metus eget eros.</p>
    <p class="program"><b>Tiny Sparrows</b> – ages 4 to 6. A specialised martial arts program for ages 4 to 6.</p>
    <p class="program"><b>Kids Kung Fu</b> – ages 6 to 11. Practical, Responsible Instruction. Plus, we specialize in powerful character development skills in a positive environment. Kids learn self defence NOT fighting, anti bullying techniques.</p>
    <p class="program"><b>Youth Kung Fu</b> – ages 11 to 15. The ultimate way to Build Confidence, Self-Esteem, Self-Discipline, and Athletic Skills, while learning self defence in a tradition style Martial Arts.</p>
    <p class="program"><b>Adults Shaolin Kung Fu</b> - ages 15 &amp; over. Self defence utilizing great range of punches, kicks, joint-locking, throwing and grappling techniques. The class utilizes traditional training methods designed to develop a sound mind and body.</p>
    <p class="program"><b>Wing Chun Kung Fu</b> – ages 13 &amp; over. Authentic Wing Chun Kung Fu by Lantern Gate Wing Chun in the direct lineage to Lo Wen Tsai (World famous Wing Chun Master). Effective, direct, efficient Self Defence.</p>
  </section>

  <aside class="sidebar">
    <h2>List of classes/programs</h2>
    <h3>Tiny Sparrows</h3>
    <p>ages 4 to 6. A specialised martial arts program for ages 4 to 6.</p>
    <h3>Adult Kung Fu</h3>
    <p>ages 6 to 11. Practical, Responsible Instruction. Plus, we specialize in powerful character development skills in a positive environment. Kids learn self defence NOT fighting, anti bullying techniques.</p>
    <h3>Adult Kung Fu</h3>
    <p>ages 6 to 11. Practical, Responsible Instruction. Plus, we specialize in powerful character development skills in a positive environment. Kids learn self defence NOT fighting, anti bullying techniques.</p>
    <h3>Tiny Sparrows</h3>
    <p>ages 4 to 6. A specialised martial arts program for ages 4 to 6.</p>
    <h3>Tiny Sparrows</h3>
    <p>ages 4 to 6. A specialised martial arts program for ages 4 to 6.</p>
  </aside>

  <footer class="footer">
    <ul style="left:43px"><li>Home</li><li>Programs</li><li>Timtable</li><li>Coaches</li></ul>
    <ul style="left:153px"><li>Support</li><li>FAQ</li><li>Newsletters</li><li>Social Media</li></ul>
    <ul style="left:275px"><li>Tiny Sparrows</li><li>Kids Kung Fu</li><li>Youth Kung Fu</li><li>Adults Kung Fu</li></ul>
    <ul style="left:416px"><li>Wing Chun</li><li>Tai Chi &amp; Qigong</li><li>Weaponry Classes</li><li>48 Paths of Endurance</li></ul>
    <div class="foot-mark">Copper Heron</div>
    <p class="copyright">© 2012 Company Name &nbsp;|&nbsp; All right reserved</p>
  </footer>
</body>
</html>
```